Luxury Face Oil Label

I'm looking for a simple and sophisticated design for a natural face oil that will target the luxe market. It is a pure Natural product. I have attached the logo, Velumi Organics.

Here's the Copy

LUXE FACIAL OIL

Regenerate. Hydrate. Glow

100% Natural

30ml (1.01 oz)

A complex blend of Pure Oils including Marula, Sea Buckthorn, Rosehip, Neroli, Evening primrose, Argan, Calendula, Lavender, Jojoba, Grapeseed, Baobab, Moringa and Vitamin E oil.

Produced by
Brasso Kettle Ltd
P.O box 7925-00300
Nairobi, Kenya
www.velumiorganics.example

Target Market(s)

High end

Requirements
Must have
• Simple, Please consider the bottle, which is a 30ml clear glass bottle with a gold and white pump. Image attached.
Nice to have
• Very clean designs, not too much going on.
Should not have
• Leaves and nuts.

```html
<!DOCTYPE html>
<html lang="en">
<head>
<meta charset="utf-8">
<title>Velumi Organics – Luxe Facial Oil Label</title>
<link rel="stylesheet" href="https://fonts.googleapis.com/css2?family=Cinzel:wght@400;600&family=Libre+Bodoni:wght@700&family=Questrial&display=swap">
<style>
  :root {
    --backdrop: #868072;
    --paper: #ffffff;
    --paper-shade: #e9e9ea;
    --olive-dark: #6b6a5f;
    --sage: #c2c1aa;
    --ink: #5b5a4f;
    --ink-soft: #77766d;
    --silver: #dcdcdc;
    --frame: #d6d5cc;
    --leaf-area: #ecebe4;
  }
  * { box-sizing: border-box; margin: 0; padding: 0; }
  html, body { width: 1151px; height: 1200px; overflow: hidden; }
  body { background: var(--backdrop); position: relative; }

  .label {
    position: absolute; left: 40px; top: 386px;
    width: 1071px; height: 428px;
    background: var(--paper);
    overflow: hidden;
  }
  .panel { position: absolute; top: 0; height: 340px; }
  .panel--ingredients { left: 0; width: 357px;
    background: linear-gradient(180deg, var(--paper-shade) 0%, #fafafa 40%, #f3f3f4 100%); }
  .panel--front { left: 357px; width: 357px; background: var(--paper); }
  .panel--back { left: 714px; width: 357px;
    background: linear-gradient(160deg, var(--paper-shade) 0%, #fbfbfb 45%, #f1f1f2 100%); }

  .blend-tab {
    position: absolute; left: 0; top: 130px; width: 135px; height: 87px;
    background: var(--sage); border-radius: 0 14px 14px 0;
    padding: 10px 8px 0 20px;
    font: 15px/16px "Questrial", sans-serif; color: var(--ink); text-transform: uppercase;
  }
  .oil-list {
    position: absolute; left: 150px; top: 18px; list-style: none;
    font: 15.5px/23.7px "Questrial", sans-serif; color: var(--ink-soft);
  }
  .oil-list li { display: flex; align-items: center; }
  .oil-list svg { width: 22px; height: 10px; margin-right: 11px; }

  .brand-box {
    position: absolute; border: 1px solid var(--frame); background: var(--paper);
    display: flex; align-items: center; justify-content: center; text-align: center;
    font-family: "Cinzel", serif; font-weight: 400; color: var(--ink-soft);
    text-transform: uppercase; letter-spacing: 3px;
  }
  .brand-box--front { left: 467px; top: 18px; width: 107px; height: 106px; font-size: 13px; line-height: 18px; }
  .brand-box--back { left: 832px; top: 108px; width: 121px; height: 120px; font-size: 14px; line-height: 20px; }
  .brand-box--band { left: 139px; top: 351px; width: 71px; height: 70px; font-size: 8px; line-height: 12px; letter-spacing: 1.5px; }

  .band-rule { position: absolute; left: 0; top: 335px; width: 100%; height: 5px; background: var(--olive-dark); }
  .band { position: absolute; left: 0; top: 340px; width: 100%; height: 88px; background: var(--sage); }

  .illustration {
    position: absolute; left: 596px; top: 132px; width: 120px; height: 296px;
    background: linear-gradient(180deg, var(--leaf-area) 0%, #f6f5f0 100%);
    border-radius: 60px 60px 10px 10px;
  }

  .title-main {
    position: absolute; left: 413px; top: 143px; width: 215px; height: 71px;
    background: var(--olive-dark); border-radius: 10px 34px 0 0;
    font: 700 62px/74px "Libre Bodoni", serif; color: var(--silver);
    text-align: center; letter-spacing: 1px;
  }
  .title-sub {
    position: absolute; left: 413px; top: 214px; width: 203px; height: 42px;
    background: var(--sage); border-radius: 0 0 28px 10px;
    font: 400 27px/44px "Cinzel", serif; color: var(--ink); text-align: center; letter-spacing: 1px;
  }
  .drips { position: absolute; left: 508px; top: 256px; width: 24px; height: 76px; }

  .natural-badge {
    position: absolute; left: 391px; top: 305px; width: 72px; height: 36px;
    background: var(--olive-dark); border-radius: 36px 36px 0 0;
    color: #fff; text-align: center; font-family: "Libre Bodoni", serif;
  }
  .natural-badge .pct { display: block; font-size: 15px; line-height: 15px; padding-top: 8px; }
  .natural-badge .word { display: block; font-size: 8px; line-height: 9px; letter-spacing: .5px; }

  .benefits {
    position: absolute; left: 388px; top: 350px; list-style: none;
    font: 400 17px/23.5px "Cinzel", serif; color: var(--ink);
  }
  .benefits li::before { content: "›"; font-size: 12px; margin-right: 5px; color: var(--ink-soft); }

  .volume {
    position: absolute; left: 560px; top: 366px; width: 58px; text-align: center;
    font: 400 17px/17px "Libre Bodoni", serif; color: var(--ink);
  }
  .volume small { display: block; font-size: 8px; line-height: 11px; }

  .producer {
    position: absolute; left: 790px; top: 352px; width: 205px; text-align: center;
    font: 10.5px/13.6px "Questrial", sans-serif; color: var(--ink-soft);
  }
  .producer strong { font-weight: 700; }
</style>
</head>
<body>
<main class="label">
  <section class="panel panel--ingredients">
    <p class="blend-tab">A complex blend of pure oils including</p>
    <ul class="oil-list">
      <li><svg viewBox="0 0 22 10"><path d="M1 5h18M14 1l5 4-5 4" stroke="#9a998f" stroke-width="1.3" fill="none"/></svg>Marula,</li>
      <li><svg viewBox="0 0 22 10"><path d="M1 5h18M14 1l5 4-5 4" stroke="#9a998f" stroke-width="1.3" fill="none"/></svg>Sea Buckthorn,</li>
      <li><svg viewBox="0 0 22 10"><path d="M1 5h18M14 1l5 4-5 4" stroke="#9a998f" stroke-width="1.3" fill="none"/></svg>Rosehip,</li>
      <li><svg viewBox="0 0 22 10"><path d="M1 5h18M14 1l5 4-5 4" stroke="#9a998f" stroke-width="1.3" fill="none"/></svg>Neroli,</li>
      <li><svg viewBox="0 0 22 10"><path d="M1 5h18M14 1l5 4-5 4" stroke="#9a998f" stroke-width="1.3" fill="none"/></svg>Evening primrose,</li>
      <li><svg viewBox="0 0 22 10"><path d="M1 5h18M14 1l5 4-5 4" stroke="#9a998f" stroke-width="1.3" fill="none"/></svg>Argan,</li>
      <li><svg viewBox="0 0 22 10"><path d="M1 5h18M14 1l5 4-5 4" stroke="#9a998f" stroke-width="1.3" fill="none"/></svg>Calendula,</li>
      <li><svg viewBox="0 0 22 10"><path d="M1 5h18M14 1l5 4-5 4" stroke="#9a998f" stroke-width="1.3" fill="none"/></svg>Lavender,</li>
      <li><svg viewBox="0 0 22 10"><path d="M1 5h18M14 1l5 4-5 4" stroke="#9a998f" stroke-width="1.3" fill="none"/></svg>Jojoba,</li>
      <li><svg viewBox="0 0 22 10"><path d="M1 5h18M14 1l5 4-5 4" stroke="#9a998f" stroke-width="1.3" fill="none"/></svg>Grapeseed,</li>
      <li><svg viewBox="0 0 22 10"><path d="M1 5h18M14 1l5 4-5 4" stroke="#9a998f" stroke-width="1.3" fill="none"/></svg>Baobab,</li>
      <li><svg viewBox="0 0 22 10"><path d="M1 5h18M14 1l5 4-5 4" stroke="#9a998f" stroke-width="1.3" fill="none"/></svg>Moringa</li>
      <li><svg viewBox="0 0 22 10"><path d="M1 5h18M14 1l5 4-5 4" stroke="#9a998f" stroke-width="1.3" fill="none"/></svg>Vitamin E oil.</li>
    </ul>
  </section>
  <section class="panel panel--front"></section>
  <section class="panel panel--back"></section>

  <div class="brand-box brand-box--front">Velumi Organics</div>
  <div class="brand-box brand-box--back">Velumi Organics</div>

  <div class="band-rule"></div>
  <div class="band"></div>

  <div class="illustration" role="img" aria-label="Line drawing of a botanical sprig in grey outline"></div>

  <h1 class="title-main">LUXE</h1>
  <h2 class="title-sub">FACIAL OIL</h2>
  <svg class="drips" viewBox="0 0 24 76" aria-hidden="true">
    <path d="M12 0 C12 8 19 14 19 20 A7 7 0 0 1 5 20 C5 14 12 8 12 0Z" fill="#dcdbd0"/>
    <path d="M12 22 C12 30 19 36 19 42 A7 7 0 0 1 5 42 C5 36 12 30 12 22Z" fill="#cfcebf"/>
    <path d="M12 46 C12 54 20 60 20 67 A8 8 0 0 1 4 67 C4 60 12 54 12 46Z" fill="#c2c1aa"/>
  </svg>

  <div class="natural-badge"><span class="pct">100%</span><span class="word">NATURAL</span></div>

  <div class="brand-box brand-box--band">Velumi Organics</div>

  <ul class="benefits">
    <li>Regenerate</li>
    <li>Hydrate</li>
    <li>Glow</li>
  </ul>

  <p class="volume">30ML<small>(1.01 oz)</small></p>

  <address class="producer">
    Produced by<br>
    <strong>Brasso Kettle Ltd</strong><br>
    P.O box 7925-00300<br>
    Nairobi, Kenya<br>
    <strong>www.velumiorganics.example</strong>
  </address>
</main>
</body>
</html>
```